Plotvista Caribbean

We need a vibrant, user friendly and exciting website for our land search company called "plotVista" This application will help individuals locate and or list lots for sale within the Caribbean. We will offer a small cash back incentive to buyers that purchase land from our site, and we will charge a 1%-2% success fee to our sellers once a successful transaction is made. We would like to become a match making site, matching buyers and sellers on our platform. We will also include a service directory and marketing advertisement spot for other service providers for a fee. We would like to see a webdesign incorporating Caribbean colors (blue, green and yellow) with very modern clean lines, very picturesque and easy to use.

Industry/Entity Type

Real Estate

Coding

Number of Pages Required

5+ page

Font styles to use
Sans Serif

Colors
ffffff
85acd3
b768aa
dbdbdb

Requirements
Nice to have
• Scenic photos of the ocean and beautiful landscape

```html
<!DOCTYPE html>
<html lang="en">
<head>
<meta charset="utf-8">
<title>plotVista — Find the land you are looking for</title>
<link href="https://fonts.googleapis.com/css2?family=Montserrat:wght@600;700&family=Open+Sans:wght@400;600;700&display=swap" rel="stylesheet">
<style>
:root{
  --white:#ffffff;
  --blue:#85acd3;
  --blue-band:#8aadd6;
  --blue-soft:#a7c1df;
  --purple:#b768aa;
  --gray:#dbdbdb;
  --gray-bg:#eeeef0;
  --text:#555a60;
  --dark:#2f3338;
}
*{box-sizing:border-box;margin:0;padding:0}
html,body{width:1200px;height:3321px;overflow:hidden}
body{position:relative;background:var(--white);font-family:"Open Sans",Arial,sans-serif;color:var(--text)}
.abs{position:absolute}

/* hero */
.hero{left:0;top:0;width:1200px;height:704px;background:linear-gradient(180deg,#4a6576 0%,#1f8aa6 100%)}
.logo{font-family:"Montserrat",sans-serif;font-weight:700;font-size:31px;color:var(--white);letter-spacing:-.3px}
.nav{top:24px;left:538px;display:flex}
.nav a{display:block;font-family:"Montserrat",sans-serif;font-weight:700;font-size:12px;color:var(--white);text-decoration:none;padding:6px 10px;height:26px;line-height:14px;margin-right:12px;text-transform:uppercase}
.nav a.active{background:var(--white);color:var(--purple)}
.hero-title{left:133px;top:384px;font-family:"Montserrat",sans-serif;font-weight:700;font-size:40px;line-height:50px;color:var(--white);letter-spacing:.5px}
.search-frame{left:133px;top:516px;width:571px;height:82px;background:rgba(20,30,40,.75);padding:15px 14px}
.search-box{width:100%;height:52px;background:var(--white);display:flex;align-items:center;padding:0 8px 0 18px}
.search-box span{flex:1;font-family:"Montserrat",sans-serif;font-weight:700;font-size:12px;color:#333;margin-left:10px}
.search-btn{background:var(--purple);color:var(--white);font-family:"Montserrat",sans-serif;font-weight:700;font-size:13px;width:96px;height:36px;display:flex;align-items:center;justify-content:center}
.hero-dots{left:1057px;top:658px;display:flex;gap:11px}
.hero-dots i{width:9px;height:9px;border-radius:50%;background:var(--white);display:block}
.hero-dots i.on{background:transparent;border:2px solid var(--white);width:11px;height:11px;margin-top:-1px}

/* feature band */
.band{left:0;top:704px;width:1200px;height:164px;background:var(--blue-band);display:flex}
.band-item{width:300px;height:100%;position:relative;border-right:1px solid rgba(255,255,255,.25)}
.band-item:last-child{border-right:0}
.band-item svg{position:absolute;left:40px;top:52px}
.band-item h3{position:absolute;left:104px;top:48px;font-family:"Montserrat",sans-serif;font-weight:700;font-size:13px;color:var(--white);text-transform:uppercase}
.band-item p{position:absolute;left:104px;top:80px;font-size:11.5px;line-height:20px;color:var(--white);width:130px}

/* featured */
.section-title{width:1200px;left:0;text-align:center;font-family:"Montserrat",sans-serif;font-weight:700;font-size:31px;color:var(--purple);text-transform:uppercase}
.title-rule{left:573px;top:996px;width:54px;height:2px;background:var(--purple)}
.card{top:1043px;width:299px}
.card-photo{width:299px;height:234px}
.card h4{margin-top:26px;font-family:"Montserrat",sans-serif;font-weight:700;font-size:17px;color:var(--blue);text-transform:uppercase}
.card p{margin-top:8px;font-size:11.5px;line-height:22px;color:#555}
.price-box{margin-top:14px;width:262px;height:58px;border:3px solid var(--purple);position:relative;padding:7px 0 0 12px}
.price-box small{display:block;font-family:"Montserrat",sans-serif;font-weight:700;font-size:10px;color:#333}
.price-box strong{display:block;font-family:"Montserrat",sans-serif;font-weight:600;font-size:20px;color:var(--purple);line-height:24px}
.read-more{position:absolute;right:10px;top:10px;width:88px;height:30px;background:var(--blue);color:var(--white);font-family:"Montserrat",sans-serif;font-weight:700;font-size:10px;display:flex;align-items:center;justify-content:center;text-transform:uppercase}
.pager{left:553px;top:1496px;display:flex;gap:6px}
.pager i{display:block;width:11px;height:11px;background:var(--blue-soft)}
.pager i.on{background:var(--blue)}

/* why choose */
.why-bg{left:0;top:1568px;width:1200px;height:617px;background:var(--gray-bg)}
.why-title{top:1615px;left:0;width:1200px;text-align:center;font-family:"Montserrat",sans-serif;font-weight:700;text-transform:uppercase}
.why-title .l1{display:block;font-size:31px;color:var(--purple);line-height:40px}
.why-title .l2{display:block;font-size:38px;color:var(--blue);line-height:48px}
.why-photo{left:219px;top:1747px;width:760px;height:343px;background:linear-gradient(180deg,#4f7a48 0%,#1f93ac 100%)}
.why-cards{left:221px;top:2090px;width:756px;height:173px;background:var(--white);display:flex;z-index:2}
.why-card{flex:1;text-align:center;border-right:1px solid var(--gray);position:relative;padding-top:62px}
.why-card:last-child{border-right:0}
.why-icon{position:absolute;left:50%;top:-51px;margin-left:-43px;width:86px;height:86px;border-radius:50%;background:var(--purple);border:4px solid var(--white);display:flex;align-items:center;justify-content:center}
.why-card h4{font-family:"Montserrat",sans-serif;font-weight:700;font-size:12.5px;color:var(--blue);text-transform:uppercase}
.why-card p{margin:14px auto 0;width:200px;font-size:11px;line-height:20px;color:#444}

/* testimonials */
.testi{left:0;top:2185px;width:1200px;height:463px;background:var(--blue-soft)}
.testi h2{position:absolute;top:140px;width:1200px;text-align:center;font-family:"Montserrat",sans-serif;font-weight:700;font-size:31px;color:var(--white)}
.testi blockquote{position:absolute;top:212px;left:300px;width:600px;text-align:center;font-size:13.5px;line-height:29px;color:#3f4750}
.arrow{position:absolute;top:2413px;width:50px;height:50px;border:2px solid rgba(255,255,255,.8);border-radius:50%}
.testi-rule{position:absolute;left:524px;top:335px;width:152px;height:2px;background:var(--white)}
.testi cite{position:absolute;top:360px;width:1200px;text-align:center;font-style:normal;font-family:"Montserrat",sans-serif;font-weight:700;font-size:12px;line-height:18px;color:var(--white)}

/* call to action */
.cta-photo{left:0;top:2648px;width:1200px;height:330px;background:linear-gradient(180deg,#3d4036 0%,#5a7440 100%)}
.cta-title{left:0;top:2730px;width:1200px;text-align:center;font-family:"Montserrat",sans-serif;font-weight:700;font-size:27px;color:var(--white)}
.cta-text{left:0;top:2778px;width:1200px;text-align:center;font-size:13.5px;color:rgba(255,255,255,.85)}
.cta-btn{left:505px;top:2838px;width:190px;height:56px;background:var(--purple);color:var(--white);font-family:"Montserrat",sans-serif;font-weight:700;font-size:17px;display:flex;align-items:center;justify-content:center}

/* footer */
.foot-logo{left:132px;top:3045px;font-family:"Montserrat",sans-serif;font-weight:700;font-size:43px;color:var(--purple)}
.follow{left:139px;top:3148px;display:flex;align-items:center;gap:8px;font-family:"Montserrat",sans-serif;font-weight:700;font-size:11px;color:var(--purple)}
.follow span{margin-right:14px}
.follow i{display:block;width:30px;height:30px;border-radius:50%}
.foot-col h5{font-family:"Montserrat",sans-serif;font-weight:700;font-size:11px;color:var(--purple);text-transform:uppercase;margin-bottom:12px}
.foot-col li{list-style:none;font-size:12px;line-height:19.5px;color:#555}
.newsletter-input{left:824px;top:3084px;width:245px;height:40px;border:1.5px solid #ccc;padding:11px 12px;font-size:12px;color:#777}
.newsletter-btn{left:983px;top:3137px;width:86px;height:34px;background:var(--purple);color:var(--white);font-family:"Montserrat",sans-serif;font-weight:700;font-size:14px;display:flex;align-items:center;justify-content:center}
.foot-rule{left:131px;top:3228px;width:938px;height:1px;background:var(--gray)}
.copyright{left:0;top:3258px;width:1200px;text-align:center;font-size:11.5px;color:#555}
</style>
</head>
<body>

<!-- hero -->
<div class="abs hero" role="img" aria-label="Scenic photo of mountains above a turquoise lake with pine forest"></div>
<div class="abs logo" style="left:131px;top:14px">plotVista</div>
<nav class="abs nav">
  <a class="active">Home</a><a>About Us</a><a>Services</a><a>Buy &amp; Sell</a><a>Blog</a><a>Contact Us</a>
</nav>
<h1 class="abs hero-title">FIND THE LAND YOU<br>ARE LOOKING FOR</h1>
<div class="abs search-frame">
  <div class="search-box">
    <svg width="12" height="12" viewBox="0 0 12 12"><circle cx="5" cy="5" r="3.8" fill="none" stroke="#333" stroke-width="1.8"/><line x1="7.8" y1="7.8" x2="11" y2="11" stroke="#333" stroke-width="2"/></svg>
    <span>SEARCH HERE</span>
    <div class="search-btn">SEARCH</div>
  </div>
</div>
<div class="abs hero-dots"><i></i><i class="on"></i><i></i><i></i><i></i></div>

<!-- feature band -->
<section class="abs band">
  <div class="band-item">
    <svg width="36" height="44" viewBox="0 0 36 44"><circle cx="18" cy="11" r="9" fill="#fff"/><path d="M2 44c0-12 7-19 16-19s16 7 16 19z" fill="#fff"/></svg>
    <h3>Buyers &amp; Sellers</h3><p>Lorem Ipsum is simply dummy text</p>
  </div>
  <div class="band-item">
    <svg width="54" height="46" viewBox="0 0 54 46"><circle cx="27" cy="9" r="7" fill="#fff"/><circle cx="11" cy="13" r="6" fill="#fff"/><circle cx="43" cy="13" r="6" fill="#fff"/><rect x="19" y="19" width="16" height="27" rx="4" fill="#fff"/><rect x="4" y="22" width="13" height="22" rx="4" fill="#fff"/><rect x="37" y="22" width="13" height="22" rx="4" fill="#fff"/></svg>
    <h3>Meet the Team</h3><p>Lorem Ipsum is simply dummy text</p>
  </div>
  <div class="band-item">
    <svg width="34" height="48" viewBox="0 0 34 48"><path d="M17 2C9 2 3 8 3 16c0 11 14 29 14 29s14-18 14-29C31 8 25 2 17 2z" fill="none" stroke="#fff" stroke-width="3"/><circle cx="17" cy="16" r="5" fill="none" stroke="#fff" stroke-width="3"/></svg>
    <h3>About the Area</h3><p>Lorem Ipsum is simply dummy text</p>
  </div>
  <div class="band-item">
    <svg width="48" height="48" viewBox="0 0 48 48"><rect x="22" y="2" width="4" height="44" fill="#fff"/><rect x="2" y="22" width="44" height="4" fill="#fff"/></svg>
    <h3>More Info</h3><p>Lorem Ipsum is simply dummy text</p>
  </div>
</section>

<!-- featured properties -->
<h2 class="abs section-title" style="top:930px">Featured Properties</h2>
<div class="abs title-rule"></div>

<article class="abs card" style="left:131px">
  <div class="card-photo" role="img" aria-label="Photo of a green meadow under a blue sky" style="background:linear-gradient(180deg,#4f86c8 0%,#6f9a3e 100%)"></div>
  <h4>Heading 1</h4>
  <p>It is a long established fact that a reader will be distracted by the readable content</p>
  <div class="price-box"><small>STARTING FROM</small><strong>$15000.000</strong><div class="read-more">Read More</div></div>
</article>
<article class="abs card" style="left:451px">
  <div class="card-photo" role="img" aria-label="Aerial photo of green land" style="background:#7ba23a"></div>
  <h4>Heading 2</h4>
  <p>It is a long established fact that a reader will be distracted by the readable content</p>
  <div class="price-box"><small>STARTING FROM</small><strong>$12154.000</strong><div class="read-more">Read More</div></div>
</article>
<article class="abs card" style="left:768px">
  <div class="card-photo" role="img" aria-label="Photo of a dry open plot at sunset" style="background:linear-gradient(180deg,#d9cfae 0%,#9a7653 100%)"></div>
  <h4>Heading 3</h4>
  <p>It is a long established fact that a reader will be distracted by the readable content</p>
  <div class="price-box"><small>STARTING FROM</small><strong>$11256.000</strong><div class="read-more">Read More</div></div>
</article>
<div class="abs pager"><i class="on"></i><i></i><i></i><i></i><i></i></div>

<!-- why choose -->
<div class="abs why-bg"></div>
<h2 class="abs why-title"><span class="l1">Why Choose</span><span class="l2">plotVista</span></h2>
<div class="abs why-photo" role="img" aria-label="Scenic photo of green coastal cliffs over a turquoise sea"></div>

<!-- testimonials -->
<section class="abs testi">
  <h2>TESTIMONIALS</h2>
  <blockquote>Lorem Ipsum is simply dummy text of the printing and typesetting industry. Lorem Ipsum has been the industry's standard dummy text ever since the 1500s, when an unknown printer took a galley of type and scrambled</blockquote>
  <div class="testi-rule"></div>
  <cite>MARCUS DELANEY<br>ENGLAND</cite>
</section>
<div class="abs arrow" style="left:199px"><svg width="46" height="46" viewBox="0 0 46 46"><path d="M26 16l-7 7 7 7" fill="none" stroke="#fff" stroke-width="2.5"/></svg></div>
<div class="abs arrow" style="left:940px"><svg width="46" height="46" viewBox="0 0 46 46"><path d="M20 16l7 7-7 7" fill="none" stroke="#fff" stroke-width="2.5"/></svg></div>

<div class="abs why-cards">
  <div class="why-card">
    <div class="why-icon"><svg width="34" height="34" viewBox="0 0 34 34"><rect x="3" y="14" width="7" height="17" fill="#fff"/><path d="M12 15l6-11c3 0 4 2 3 6l-1 4h9c2 0 3 2 2 4l-3 11c-1 2-2 2-4 2H12z" fill="#fff"/></svg></div>
    <h4>Quality</h4><p>It is a long established fact that a reader will be distracted by the readable content</p>
  </div>
  <div class="why-card">
    <div class="why-icon"><svg width="34" height="34" viewBox="0 0 34 34"><path d="M5 20v-4a12 12 0 0 1 24 0v4" fill="none" stroke="#fff" stroke-width="3.5"/><rect x="3" y="18" width="8" height="12" rx="2" fill="#fff"/><rect x="23" y="18" width="8" height="12" rx="2" fill="#fff"/></svg></div>
    <h4>Get Support</h4><p>It is a long established fact that a reader will be distracted by the readable content</p>
  </div>
  <div class="why-card">
    <div class="why-icon"><svg width="34" height="34" viewBox="0 0 34 34"><rect x="3" y="7" width="22" height="24" rx="2" fill="none" stroke="#fff" stroke-width="3"/><path d="M14 21l2-6 13-13 4 4-13 13z" fill="#fff"/></svg></div>
    <h4>Signup With Us</h4><p>It is a long established fact that a reader will be distracted by the readable content</p>
  </div>
</div>

<!-- call to action -->
<div class="abs cta-photo" role="img" aria-label="Background photo of rolling green hills at dusk"></div>
<h2 class="abs cta-title">SMALL CASH BACK INCENTIVE TO BUYERS</h2>
<p class="abs cta-text">Lorem Ipsum is simply dummy text of the printing and typesetting industry. Lorem Ipsum has been the industry</p>
<div class="abs cta-btn">LEARN MORE</div>

<!-- footer -->
<div class="abs foot-logo">plotVista</div>
<div class="abs follow"><span>FOLLOW US :</span><i style="background:#3b5b9a"></i><i style="background:#2aa3e0"></i><i style="background:#e0684f"></i></div>
<div class="abs foot-col" style="left:434px;top:3044px">
  <h5>Menu</h5>
  <ul><li>Home</li><li>About</li><li>Services</li><li>Testimonials</li><li>Contact us</li></ul>
</div>
<div class="abs foot-col" style="left:596px;top:3044px">
  <h5>Contact Us</h5>
  <ul><li>48 Coral Bay Road</li><li>Seabrook, FL 32001</li><li>T : 555.014.2290</li><li>E : info@plotvista.com</li></ul>
</div>
<div class="abs foot-col" style="left:824px;top:3044px"><h5>Newsletter Signup</h5></div>
<div class="abs newsletter-input">E mail id</div>
<div class="abs newsletter-btn">SIGNUP</div>
<div class="abs foot-rule"></div>
<div class="abs copyright">Copyrights @ 2017 All Rights Reserved</div>

</body>
</html>
```